Fernbrook Vale Executive Development Workshop Series

* Had error in first version of MS Word doc and have re-uploaded - twelve subject areas, not nine *
I'd like a flyer to print to hand out and post on my website fernbrookvale.com to advertise a workshop series I'm launching. I'd like it to build strongly on the wonderful logo you did and Scottish theme...and to have the same "feel" as my website. fernbrookvale.com
It should be 8.5x11, single sided. Not sure if I should use full color glossy or two-color on nice paper. Regardless, I will most likely have it done on a color copier and will not put it on a printing press.
I have typed up a document with all the information in a MS Word file, but need you to lay it out in an aesthetically pleasing way. I have attached that MS Word file.
I am also attaching a handful of similar flyer documents from other non-competing coaches in my network. I think they all have their merits, but leave me under-whelmed.
I'm also attaching a picture of me and some pictures of Scotland my parents took about 10 years ago. I'm reluctantly open to stock photos, just not too obvious or hackneyed (if that word can be applied to pictures as well as expressions).
Lastly, this workshop series will be an ongoing thing, so I'd like to be able to make minor edits myself with things like new dates or topics.
Thank you!
Target Market(s)
Small business owners and emerging leaders with large companies
Colors
Designer to choose colors to be used in the design.
Requirements
Should not have
- Obviously stock photos

```html
<!DOCTYPE html>
<html lang="en">
<head>
<meta charset="utf-8">
<title>Fernbrook Vale Executive Development Workshop Series</title>
<link rel="stylesheet" href="https://fonts.googleapis.com/css2?family=Cinzel:wght@500&family=Great+Vibes&family=Roboto+Condensed:ital,wght@0,400;0,700;1,700&family=Cabin:wght@400;600&family=Montserrat:wght@500;700&display=swap">
<style>
  :root {
    --olive: #6b733f;
    --olive-dark: #56602f;
    --title-grey: #555a55;
    --text: #2f2f2f;
    --row-bg: #ececec;
    --page-bg: #e9e6df;
    --paper: #ffffff;
  }
  * { box-sizing: border-box; margin: 0; padding: 0; }
  html, body { width: 1200px; height: 1200px; overflow: hidden; background: var(--page-bg); }
  .canvas { position: relative; width: 1200px; height: 1200px; overflow: hidden; }
  .flyer {
    position: absolute; left: 152px; top: 20px;
    width: 1013px; height: 1312px;
    transform: scale(0.884); transform-origin: top left;
    background: var(--paper);
    font-family: "Cabin", sans-serif; color: var(--text);
    box-shadow: 0 6px 20px rgba(0,0,0,.18);
  }
  .abs { position: absolute; }

  .brand { left: 70px; top: 110px; width: 210px; text-align: center; }
  .brand-mark { width: 22px; height: 22px; border-radius: 50%; background: var(--olive); margin: 0 auto 10px; }
  .brand-name { font-family: "Cabin", sans-serif; font-weight: 600; font-size: 30px; color: var(--olive-dark); line-height: 1.1; }

  .title-top { left: 400px; top: 40px; width: 566px; text-align: right; font-family: "Cinzel", serif; font-weight: 500; font-size: 37px; color: var(--title-grey); letter-spacing: 1px; white-space: nowrap; }
  .title-script { left: 400px; top: 78px; width: 566px; text-align: right; font-family: "Great Vibes", cursive; font-size: 56px; color: var(--olive-dark); white-space: nowrap; }
  .title-rule { left: 405px; top: 153px; width: 350px; height: 2px; background: var(--title-grey); }
  .title-sub { left: 760px; top: 132px; width: 206px; text-align: right; font-family: "Roboto Condensed", sans-serif; font-style: italic; font-weight: 700; font-size: 32px; color: var(--title-grey); }

  .hero { left: 0; top: 200px; width: 1013px; height: 238px;
    background: linear-gradient(180deg, #c9ccc8 0%, #9aa08e 35%, #8f9451 60%, #b39a3e 85%, #a88a35 100%); }
  .hero-band { left: 0; top: 438px; width: 1013px; height: 8px; background: var(--olive); }

  .intro { left: 47px; top: 466px; width: 919px; font-size: 14.6px; line-height: 18px; text-align: justify; }
  .intro p + p { margin-top: 9px; text-align: left; }

  .schedule { left: 47px; top: 592px; width: 919px; height: 316px; border: 1px solid #555; padding: 4px 5px; }
  .schedule-row { display: flex; height: 25.6px; gap: 6px; }
  .schedule-date { width: 89px; height: 23px; background: var(--olive); color: #fff; font-family: "Roboto Condensed", sans-serif; font-size: 13.5px; line-height: 23px; padding-left: 16px; white-space: nowrap; }
  .schedule-topic { flex: 1; height: 23px; background: var(--row-bg); font-size: 13.6px; line-height: 23px; padding-left: 27px; white-space: nowrap; }
  .schedule-shadow { left: 70px; top: 910px; width: 870px; height: 14px; background: radial-gradient(ellipse at top, rgba(0,0,0,.18), rgba(0,0,0,0) 70%); }

  .col-head { font-family: "Roboto Condensed", sans-serif; font-weight: 700; font-size: 20px; color: #222; white-space: nowrap; }
  .includes { left: 47px; top: 940px; width: 443px; }
  .includes h3 { font-weight: 600; font-size: 17px; margin-top: 12px; }
  .includes h3:first-of-type { margin-top: 14px; }
  .includes p { font-size: 14.6px; line-height: 18px; margin-top: 4px; }
  .includes p.trust { margin-top: 32px; text-align: justify; }

  .register { left: 524px; top: 940px; width: 442px; }
  .register-links { display: flex; justify-content: space-between; margin-top: 14px; font-size: 15px; }
  .register-links span { display: flex; align-items: center; gap: 9px; }
  .price { left: 524px; top: 1017px; width: 489px; height: 78px; background: var(--olive); border-radius: 18px 0 0 18px; color: #fff; padding: 8px 0 0 22px; font-family: "Montserrat", sans-serif; }
  .price-main { font-weight: 700; font-size: 27px; line-height: 32px; }
  .price-sub { font-weight: 500; font-size: 23px; line-height: 28px; }
  .venue { left: 524px; top: 1122px; width: 442px; font-size: 14.6px; line-height: 18px; text-align: justify; }
  .venue p + p { margin-top: 14px; }

  .footer { left: 0; top: 1252px; width: 1013px; height: 60px; background: var(--olive); color: #fff; display: flex; align-items: center; justify-content: space-between; padding: 0 47px; font-size: 15px; }
  .footer span { display: flex; align-items: center; gap: 8px; white-space: nowrap; }
  .footer svg { fill: none; stroke: #fff; stroke-width: 1.6; }
</style>
</head>
<body>
<div class="canvas">
  <div class="flyer">
    <div class="abs brand">
      <div class="brand-mark"></div>
      <div class="brand-name">Fernbrook Vale</div>
    </div>

    <div class="abs title-top">FERNBROOK VALE EXECUTIVE</div>
    <div class="abs title-script">Development Workshop Series</div>
    <div class="abs title-rule"></div>
    <div class="abs title-sub">First Thursdays</div>

    <div class="abs hero" role="img" aria-label="Photograph of Scottish highland mountains with golden moorland and a stand of trees"></div>
    <div class="abs hero-band"></div>

    <div class="abs intro">
      <p>A positive, fresh, results-driven approach for businesses to increase profits by building confidence, command and control in owners and executives. We will use proven leadership and business strategies to improve work-life balance, buy-in, and company value. Here’s your opportunity to meet with other like-minded business owners and executives once a month in a private and confidential setting.</p>
      <p>We’ve got nine subject areas planned, and while they are all powerful, we will shift from high-level strategy topics to “where the rubber meets the road” topics.</p>
    </div>

    <div class="abs schedule">
      <div class="schedule-row"><div class="schedule-date">SEP 7, 2017</div><div class="schedule-topic">My Company Owns Me – What a CEO should and should not do</div></div>
      <div class="schedule-row"><div class="schedule-date">OCT 5, 2017</div><div class="schedule-topic">Taking Vision / Mission / Values Down To The Molecular Level Of Your Company</div></div>
      <div class="schedule-row"><div class="schedule-date">NOV 2, 2017</div><div class="schedule-topic">People Problems – The biggest waste of time and money for every small business</div></div>
      <div class="schedule-row"><div class="schedule-date">DEC 7, 2017</div><div class="schedule-topic">Value Delivery Systems – Re-think everything you think you know about creating value</div></div>
      <div class="schedule-row"><div class="schedule-date">JAN 4, 2018</div><div class="schedule-topic">Rally Your Team Around A Goal – How to create a meaningful company goal and rally the troops around it</div></div>
      <div class="schedule-row"><div class="schedule-date">FEB 1, 2018</div><div class="schedule-topic">Building Your Executive Leadership Team – You can’t succeed without one</div></div>
      <div class="schedule-row"><div class="schedule-date">MAR 1, 2018</div><div class="schedule-topic">Improve Your Outside Sales Efforts – Help your sales force to be busy AND successful</div></div>
      <div class="schedule-row"><div class="schedule-date">APR 5, 2018</div><div class="schedule-topic">Every Brain In The Game – Engage your team and build a strong culture</div></div>
      <div class="schedule-row"><div class="schedule-date">MAY 3, 2018</div><div class="schedule-topic">Repeatable Processes – Coach your employees how to get predictable results every time</div></div>
      <div class="schedule-row"><div class="schedule-date">JUN 7, 2018</div><div class="schedule-topic">Finding and Filling Profit Holes – Most small businesses waste more money than they profit</div></div>
      <div class="schedule-row"><div class="schedule-date">JUL 12, 2018 *</div><div class="schedule-topic">Put Your Payroll On A Diet – Why waste happens, what to do about it and how it helps everyone</div></div>
      <div class="schedule-row"><div class="schedule-date">AUG 2, 2018 *</div><div class="schedule-topic">Aug 2 – Truly, How Effective Are You With This Whole “Leadership” Thing?</div></div>
    </div>
    <div class="abs schedule-shadow"></div>

    <div class="abs includes">
      <div class="col-head">Each month of this monthly workshop series includes:</div>
      <h3>3-Hour Intensive Workshop :</h3>
      <p>High-energy, creative sessions with engaging and relevant business topics, peer group advisory board (master mind), and networking (9am – 12pm, dates above)</p>
      <h3>90-minute one-on-one coaching session :</h3>
      <p>To help you absorb and apply the revelations from the group sessions to your own business (mutually scheduled)</p>
      <p class="trust">Participation and trust is vital to your investment; no holding back. Due to the confidential nature of the intensive workshops, all participants will sign a confidentiality agreement. Additionally, we will only allow one company per industry to be represented.</p>
    </div>

    <div class="abs register">
      <div class="col-head">TO REGISTER, GO TO</div>
      <div class="register-links">
        <span><svg width="20" height="20" viewBox="0 0 20 20"><circle cx="10" cy="10" r="8.5" fill="none" stroke="#4e8a3a" stroke-width="1.8"/><path d="M6 10.2l2.8 2.8L14.3 7" fill="none" stroke="#4e8a3a" stroke-width="2"/></svg>fernbrookvale.com/exec-dev</span>
        <span><svg width="20" height="20" viewBox="0 0 20 20"><circle cx="10" cy="10" r="8.5" fill="none" stroke="#4e8a3a" stroke-width="1.8"/><path d="M6 10.2l2.8 2.8L14.3 7" fill="none" stroke="#4e8a3a" stroke-width="2"/></svg>click the registration link</span>
      </div>
    </div>

    <div class="abs price">
      <div class="price-main">395/MONTH OR $295/MONTH</div>
      <div class="price-sub">with a 6-month or greater commitment</div>
    </div>

    <div class="abs venue">
      <p>All monthly Intensive Workshops will be 9am – 12pm on the dates above at Millstone Coworking at 218 Harbor Lane, Ashford NC 27000</p>
      <p>All one-on-one coaching sessions will be mutually scheduled with Alan Crane once you have registered</p>
    </div>

    <div class="abs footer">
      <span><svg width="16" height="22" viewBox="0 0 16 22"><path d="M8 21s7-8 7-13A7 7 0 0 0 1 8c0 5 7 13 7 13z" fill="#fff" stroke="none"/><circle cx="8" cy="8" r="2.6" fill="#6b733f" stroke="none"/></svg>Alan Crane, Certified Professional Business Coach</span>
      <span><svg width="24" height="16" viewBox="0 0 24 16"><rect x="1" y="1" width="22" height="14" rx="1.5"/><path d="M1 1l11 8 11-8"/></svg>alan@fernbrookvale.com</span>
      <span><svg width="20" height="20" viewBox="0 0 20 20"><path d="M5 2l3 4-2 2c1 2.5 3.5 5 6 6l2-2 4 3-2 3C9 18 2 11 2 4z"/></svg>555-014-2288</span>
      <span><svg width="20" height="20" viewBox="0 0 20 20"><circle cx="10" cy="10" r="8.5"/><ellipse cx="10" cy="10" rx="3.8" ry="8.5"/><path d="M1.5 10h17M3 5.5h14M3 14.5h14"/></svg>fernbrookvale.com</span>
    </div>
  </div>
</div>
</body>
</html>
```